Chemical Distribution Company Needs a Website

We need a website designed for an existing company based in Michigan. We have grown substantially since inception and we need our website to reflect this growth. It currently has a very mom and pop feel to it. What we do is ship chemicals in Drums, Totes, Bags, Bulk Tank Trucks, and rail from our warehouses in Toledo Oh, and Chicago il. This will be a site that strictly shows what we do and will not be E-commerced based. The final design should communicate a large business with NorthAmerican reach and worldwide sourcing capabilities.

Target Market(s)

What we sell are chemicals such as acids, solvents, oils, and salts all of which are used in the manufacturing process of various products from steel to car parts to paint to car wash soaps to food. We are trying to look like a large company that has stability and track record to go after all types of industries and manufacturers

Industry/Entity Type

It Company

Number of Pages Required

5+ page

Font styles to use
Serif
Sans Serif

Requirements
Must have
• Be Formatted for WIX as that is what we use to Host and Build. Unless you have a better idea. I would also like it to be viewed on a mobile platform which it is not now.
• Tabs for:
• Home Page (similar to "www.pellwinstock.com")
• Who we are- with subtabs for (Overview, Leadership, and Capabilities)
• Chemicals- (subtabs for (overview, Chemicals A-Z) Look at Pellwinstock.com
• Metal Working Lubricants (with a drop down identical to the products tab at "www.ravenforgeoil.com"
• Contact- Very similar to www.tarvikmenta.com/contact/
• Need to have professional photos of Chemical Facilities, Bulk Tanks Trucks, Chemical Railcars, Storage Facilities filled with Drums and Totes, a Tank Farm.
Nice to have
• Want to have our site look like a combination of tarvikmenta.com, pellwinstock.com, and brolandquintec.com

```html
<!DOCTYPE html>
<html lang="en">
<head>
<meta charset="utf-8">
<title>Norvale Chemicals</title>
<link href="https://fonts.googleapis.com/css2?family=Michroma&family=Open+Sans:wght@400;600;700&family=Roboto:wght@400;500;700&display=swap" rel="stylesheet">
<style>
:root{
  --blue:#1e9be0;
  --sky:#5ac4ee;
  --navy:#143c5a;
  --teal:#2e6277;
  --panel:#3a3d40;
  --ink:#333;
  --muted:#666;
  --line:#e2e2e2;
  --white:#fff;
}
*{box-sizing:border-box;margin:0;padding:0}
html,body{width:1200px;height:3727px;overflow:hidden}
body{position:relative;background:var(--white);font-family:"Open Sans",Arial,sans-serif;color:var(--ink)}
.abs{position:absolute}
.display{font-family:"Michroma","Open Sans",sans-serif;font-weight:400}

/* header */
.topbar{left:0;top:0;width:1200px;height:82px;background:var(--white)}
.brand{left:55px;top:20px;display:flex;align-items:center;gap:12px}
.brand-dot{width:44px;height:44px;border-radius:50%;background:var(--blue)}
.brand-name{font-family:"Roboto",sans-serif;font-weight:700;font-size:26px;color:var(--navy);letter-spacing:.5px}
.contact-item{top:24px;display:flex;gap:10px;font-family:"Roboto",sans-serif;font-size:12px;line-height:16px;color:var(--ink)}
.contact-item b{font-weight:700;color:var(--navy)}
.navbar{left:0;top:82px;width:1200px;height:47px;background:rgba(22,52,76,.85);z-index:2}
.nav-link{top:0;line-height:47px;color:var(--white);font-family:"Roboto",sans-serif;font-size:16px;letter-spacing:.5px}
.social{top:18px;width:12px;height:12px;border-radius:50%;background:var(--white)}
.search{left:1073px;top:0;width:127px;height:47px;background:var(--blue);clip-path:polygon(18% 0,100% 0,100% 100%,0 100%)}

/* hero */
.hero{left:0;top:82px;width:1200px;height:651px;background:linear-gradient(180deg,#8fb6d8 0%,#c7d6e2 22%,#e6b43a 38%,#f0a91c 52%,#8e8a7e 70%,#6e7276 100%)}
.hero-caption{left:629px;top:179px;width:464px;height:194px;background:rgba(70,140,180,.7);padding:26px 26px}
.hero-caption h1{font-size:29px;line-height:38px;color:var(--white);letter-spacing:1px}
.hero-caption p{font-size:13px;color:var(--white);margin-top:10px;line-height:17px}
.hero-arrow{top:400px;width:55px;height:55px;background:rgba(0,0,0,.35);display:flex;align-items:center;justify-content:center}
.request-tab{left:820px;top:621px;width:328px;height:45px;background:var(--blue);color:var(--white);font-family:"Roboto",sans-serif;font-size:16px;font-weight:500;line-height:45px;padding-left:30px}
.feature-panel{left:55px;top:666px;width:1093px;height:179px;background:var(--panel);border-top:4px solid var(--blue)}
.feature{top:36px;display:flex;gap:16px;width:340px}
.feature h3{font-family:"Roboto",sans-serif;font-size:17px;color:var(--sky);font-weight:500;letter-spacing:.5px}
.feature p{font-size:12px;line-height:16px;color:#ddd;width:170px;margin-top:2px}

/* welcome */
.welcome-title{left:55px;top:911px;font-size:26px;color:var(--blue)}
.welcome-text{left:55px;top:957px;width:600px;font-size:12.5px;line-height:26px;color:var(--muted)}
.btn-dark{background:var(--navy);color:var(--white);font-family:"Roboto",sans-serif;font-weight:500;text-align:center}
.welcome-btn{left:537px;top:1071px;width:109px;height:35px;line-height:35px;font-size:15px}
.media{display:block}
.video{left:703px;top:889px;width:445px;height:216px;background:linear-gradient(135deg,#9bb2c2,#6f8796 55%,#c9a54a)}
.dots{display:flex;gap:14px}
.dot{width:11px;height:11px;border-radius:50%;border:1.5px solid var(--navy)}
.dot.on{background:var(--navy)}

/* stats */
.stats{left:0;top:1190px;width:1200px;height:179px;background:linear-gradient(180deg,#2aa4e6,#1a8fd6)}
.stat{top:50px;display:flex;align-items:center;gap:16px;color:var(--white)}
.stat strong{font-family:"Michroma",sans-serif;font-size:30px;font-weight:400;display:block;line-height:40px}
.stat span{font-size:11px}

/* chemicals */
.section-title{font-size:22px;color:var(--teal);letter-spacing:1px;text-align:center;width:1200px;left:0}
.section-sub{left:170px;width:860px;text-align:center;font-size:12.5px;line-height:26px;color:var(--muted)}
.pager{left:500px;top:1527px;width:200px;height:32px}
.pager-line{top:15px;height:1px;width:80px;background:var(--line)}
.pager-btn{top:0;width:32px;height:32px;border-radius:50%;border:1px solid #ccc;display:flex;align-items:center;justify-content:center}
.chem-card{top:1590px;height:216px}
.chem-card .media{width:100%;height:100%}
.chem-card h4{position:absolute;left:0;bottom:6px;width:100%;text-align:center;color:var(--white);font-family:"Roboto",sans-serif;font-size:19px;font-weight:700;letter-spacing:.5px}
.load-btn{left:470px;top:1834px;width:263px;height:62px;line-height:62px;font-size:16px}

/* services */
.services{left:0;top:1923px;width:1200px;height:412px;background:var(--teal)}
.services-title{left:78px;top:64px;font-size:26px;line-height:38px;color:var(--white);letter-spacing:1px}
.services-text{left:78px;top:152px;width:225px;font-size:12px;line-height:25px;color:#e4eef2}
.svc-card{top:40px;width:244px;height:328px;background:var(--white)}
.svc-card .media{width:100%;height:166px}
.svc-card h5{font-family:"Roboto",sans-serif;font-size:12px;font-weight:700;text-align:center;margin-top:16px;color:var(--ink)}
.svc-card p{font-size:12px;line-height:25px;padding:14px 14px 0;color:var(--ink)}
.svc-card a{display:block;padding:8px 14px 0;font-size:12px;color:var(--blue);text-decoration:none}
.dot.light{border-color:var(--sky)}
.dot.light.on{background:var(--sky)}

/* reach */
.reach-title{left:109px;top:2400px;font-family:"Roboto",sans-serif;font-size:25px;color:var(--teal);font-weight:400}
.reach-text{left:109px;top:2450px;width:640px;font-size:12px;line-height:25px;color:var(--muted)}
.contact-btn{left:112px;top:2534px;width:164px;height:40px;line-height:40px;border-radius:20px;background:var(--sky);color:var(--white);text-align:center;font-family:"Roboto",sans-serif;font-weight:500;font-size:16px}
.agent{left:882px;top:2335px;width:248px;height:274px;background:linear-gradient(180deg,#f1f1f1,#d9dde2)}
.map{left:0;top:2609px;width:1200px;height:315px;background:linear-gradient(90deg,#d9d9d9,#cfcfcf 50%,#d6d6d6)}

/* regions */
.regions-intro{left:0;width:1200px;top:2954px;text-align:center;font-family:"Roboto",sans-serif;font-size:17px;line-height:27px;color:var(--navy)}
.region-tab{top:3046px;width:276px;height:45px;line-height:45px;text-align:center;font-family:"Roboto",sans-serif;font-size:17px;letter-spacing:1px;color:var(--white);background:var(--sky)}
.region-tab.active{background:var(--navy)}
.region-box{left:109px;top:3126px;width:979px;height:273px;border:1px solid var(--line)}
.country{top:20px;width:300px}
.country h6{font-family:"Roboto",sans-serif;font-size:15px;font-weight:500;color:var(--navy);letter-spacing:.5px}
.office{margin-top:14px;padding-left:14px}
.office b{display:block;font-family:"Roboto",sans-serif;font-weight:400;font-size:15px;color:var(--blue);margin-bottom:4px}
.office span{display:block;font-size:11px;line-height:20px;color:var(--ink)}

/* footer */
.footer-col{top:3470px}
.footer-col h6{font-family:"Roboto",sans-serif;font-size:15px;font-weight:500;color:var(--navy);letter-spacing:.5px;margin-bottom:12px}
.footer-col li{list-style:none;font-size:13px;line-height:21px;color:var(--ink)}
.branch{top:3508px;width:150px}
.branch b{display:block;font-family:"Roboto",sans-serif;font-weight:400;color:var(--sky);font-size:15px;margin-bottom:6px}
.branch p{font-size:11px;line-height:19px;display:flex;gap:6px}
.bottombar{left:0;top:3670px;width:1200px;height:57px;background:var(--sky);color:var(--white);font-size:11.5px;line-height:18px;padding:10px 0 0 50px;font-weight:600}
.to-top{left:1070px;top:3680px;width:56px;height:36px;background:#2b2f33;display:flex;align-items:center;justify-content:center}
</style>
</head>
<body>

<header>
  <div class="abs topbar"></div>
  <div class="abs brand"><span class="brand-dot"></span><span class="brand-name">NORVALE CHEMICALS</span></div>
  <div class="abs contact-item" style="left:790px">
    <svg width="14" height="18" viewBox="0 0 14 18"><path d="M7 0a7 7 0 0 0-7 7c0 5 7 11 7 11s7-6 7-11a7 7 0 0 0-7-7z" fill="#143c5a"/><circle cx="7" cy="7" r="2.5" fill="#fff"/></svg>
    <div><b>No. 1234, Building Name,</b><br>Chicago il, North America</div>
  </div>
  <div class="abs contact-item" style="left:994px">
    <svg width="20" height="18" viewBox="0 0 20 18"><rect width="20" height="18" rx="2" fill="#1e9be0"/><path d="M6 4c1 0 2 2 1.5 3l-1 1c1 2 2 3 4 4l1-1c1-.5 3 .5 3 1.5 0 1-1 2-2 2C8 14 4 10 4 6c0-1 1-2 2-2z" fill="#fff"/></svg>
    <div><b>+1 (123) 456-7890</b><br>info@norvalechem.com</div>
  </div>

  <nav class="abs navbar">
    <span class="abs nav-link" style="left:62px">HOME</span>
    <span class="abs nav-link" style="left:156px">WHO WE ARE</span>
    <span class="abs nav-link" style="left:320px">CHEMICALS</span>
    <span class="abs nav-link" style="left:470px">PRODUCTS</span>
    <span class="abs nav-link" style="left:616px">CONTACT</span>
    <span class="abs social" style="left:866px"></span>
    <span class="abs social" style="left:902px"></span>
    <span class="abs social" style="left:938px"></span>
    <span class="abs social" style="left:974px"></span>
    <span class="abs social" style="left:1010px"></span>
    <div class="abs search">
      <svg class="abs" style="left:读;left:56px;top:12px" width="22" height="22" viewBox="0 0 22 22"><circle cx="9" cy="9" r="7" fill="none" stroke="#fff" stroke-width="2.5"/><path d="M14 14l6 6" stroke="#fff" stroke-width="2.5"/></svg>
    </div>
  </nav>
</header>

<section class="hero-section">
  <div class="abs hero media" role="img" aria-label="Photo of a yellow rail tank car on tracks under a blue sky"></div>
  <div class="abs hero-caption">
    <h1 class="display">BEST CHEMICAL<br>SHIPPING SERVICE</h1>
    <p>we provide best services for shipping chemicals and connect with people</p>
  </div>
  <div class="abs hero-arrow" style="left:0"><svg width="14" height="22" viewBox="0 0 14 22"><path d="M11 2L3 11l8 9" fill="none" stroke="#fff" stroke-width="2.5"/></svg></div>
  <div class="abs hero-arrow" style="left:1145px"><svg width="14" height="22" viewBox="0 0 14 22"><path d="M3 2l8 9-8 9" fill="none" stroke="#fff" stroke-width="2.5"/></svg></div>
  <div class="abs request-tab">REQUEST MORE INFORMATION
    <svg class="abs" style="left:296px;top:14px" width="18" height="18" viewBox="0 0 18 18"><path d="M3 9l6-6 6 6M3 15l6-6 6 6" fill="none" stroke="#fff" stroke-width="2"/></svg>
  </div>
  <div class="abs feature-panel">
    <div class="abs feature" style="left:27px">
      <svg width="90" height="100" viewBox="0 0 90 100"><polygon points="45,2 88,26 88,74 45,98 2,74 2,26" fill="#fff"/><path d="M22 70V44l12 8v-8l12 8v-8l12 8V30h8v40z" fill="#1e9be0"/></svg>
      <div><h3>INDUSTRIES SERVED</h3><p>lorem ipsum is the dummy texct that can be replaced with the original cintent</p></div>
    </div>
    <div class="abs feature" style="left:385px">
      <svg width="90" height="100" viewBox="0 0 90 100"><polygon points="45,2 88,26 88,74 45,98 2,74 2,26" fill="#fff"/><rect x="28" y="30" width="34" height="8" rx="2" fill="#1e9be0"/><rect x="28" y="42" width="34" height="8" rx="2" fill="#1e9be0"/><path d="M26 58h22l10 8-10 8H26z" fill="#1e9be0"/></svg>
      <div><h3>FEATURED PRODUCT</h3><p>lorem ipsum is the dummy texct that can be replaced with the original cintent</p></div>
    </div>
    <div class="abs feature" style="left:742px">
      <svg width="90" height="100" viewBox="0 0 90 100"><polygon points="45,2 88,26 88,74 45,98 2,74 2,26" fill="#fff"/><circle cx="36" cy="40" r="8" fill="#1e9be0"/><circle cx="56" cy="40" r="8" fill="#1e9be0"/><path d="M22 68c0-10 6-16 14-16s14 6 14 16zM42 68c0-10 6-16 14-16s14 6 14 16z" fill="#1e9be0"/></svg>
      <div><h3>PARTNERS &amp; SUPPLY</h3><p>lorem ipsum is the dummy texct that can be replaced with the original cintent</p></div>
    </div>
  </div>
</section>

<section class="welcome">
  <h2 class="abs welcome-title display">WELCOME TO OUR WEBSITE!</h2>
  <p class="abs welcome-text">Lorem Ipsum is simply dummy text of the printing and typesetting industry. Lorem Ipsum has been the industry's standard dummy text ever since the 1500s, when an unknown printer took a galley of type and scrambled it to make a type specimen book. It has survived not only five centuries, but also the leap into electronic typesetting.</p>
  <div class="abs btn-dark welcome-btn">Read more</div>
  <div class="abs video media" role="img" aria-label="Video still of a worker in a hard hat at a chemical plant"></div>
  <svg class="abs" style="left:892px;top:962px" width="66" height="66" viewBox="0 0 66 66"><circle cx="33" cy="33" r="31" fill="rgba(255,255,255,.9)"/><path d="M26 20l20 13-20 13z" fill="#143c5a"/></svg>
  <div class="abs dots" style="left:858px;top:1138px"><span class="dot on"></span><span class="dot"></span><span class="dot"></span><span class="dot"></span></div>
</section>

<section class="abs stats">
  <div class="abs stat" style="left:70px">
    <svg width="76" height="76" viewBox="0 0 76 76" fill="none" stroke="#fff" stroke-width="3"><circle cx="38" cy="38" r="32"/><ellipse cx="38" cy="38" rx="14" ry="32"/><path d="M6 38h64M12 22h52M12 54h52"/></svg>
    <div><strong>1234+</strong><span>Clients worldwide</span></div>
  </div>
  <div class="abs stat" style="left:375px">
    <svg width="70" height="76" viewBox="0 0 70 76" fill="none" stroke="#fff" stroke-width="3"><ellipse cx="35" cy="38" rx="32" ry="11"/><ellipse cx="35" cy="38" rx="32" ry="11" transform="rotate(60 35 38)"/><ellipse cx="35" cy="38" rx="32" ry="11" transform="rotate(-60 35 38)"/><circle cx="35" cy="38" r="4" fill="#fff"/></svg>
    <div><strong>123</strong><span>chemical services</span></div>
  </div>
  <div class="abs stat" style="left:651px">
    <svg width="92" height="70" viewBox="0 0 92 70"><rect x="2" y="8" width="52" height="42" rx="4" fill="#fff"/><path d="M56 22h18l14 16v12H56z" fill="#fff"/><circle cx="20" cy="56" r="9" fill="#fff" stroke="#1e9be0" stroke-width="4"/><circle cx="72" cy="56" r="9" fill="#fff" stroke="#1e9be0" stroke-width="4"/><circle cx="28" cy="28" r="13" fill="none" stroke="#1e9be0" stroke-width="3"/><path d="M28 20v8h6" stroke="#1e9be0" stroke-width="3" fill="none"/></svg>
    <div><strong>99%</strong><span>on-time delivery</span></div>
  </div>
  <div class="abs stat" style="left:958px">
    <svg width="92" height="76" viewBox="0 0 92 76" fill="#fff"><circle cx="46" cy="22" r="16"/><path d="M16 74c0-20 13-32 30-32s30 12 30 32z"/><circle cx="16" cy="30" r="10"/><circle cx="76" cy="30" r="10"/><path d="M0 68c0-14 7-22 16-22 4 0 7 1 9 3-6 6-9 12-10 19zM92 68c0-14-7-22-16-22-4 0-7 1-9 3 6 6 9 12 10 19z"/></svg>
    <div><strong>123+</strong><span>people in team</span></div>
  </div>
</section>

<section class="chemicals">
  <h2 class="abs section-title display" style="top:1408px">CHEMICALS</h2>
  <p class="abs section-sub" style="top:1452px">We provide different types of chemicals that are needed for many industries for their daily services. We make sure to serve the best chemicals and trasport then with care</p>
  <div class="abs pager">
    <span class="abs pager-line" style="left:-20px"></span>
    <span class="abs pager-line" style="left:140px"></span>
    <span class="abs pager-btn" style="left:66px"><svg width="8" height="12" viewBox="0 0 8 12"><path d="M6 1L1 6l5 5" fill="none" stroke="#333" stroke-width="1.6"/></svg></span>
    <span class="abs pager-btn" style="left:102px"><svg width="8" height="12" viewBox="0 0 8 12"><path d="M2 1l5 5-5 5" fill="none" stroke="#333" stroke-width="1.6"/></svg></span>
  </div>
  <div class="abs chem-card" style="left:55px;width:350px"><div class="media" role="img" aria-label="Photo of golden oil pouring from a can" style="background:linear-gradient(135deg,#c9c36a,#8f8b34 50%,#3b3a22)"></div><h4>LUBRICANTS</h4></div>
  <div class="abs chem-card" style="left:422px;width:353px"><div class="media" role="img" aria-label="Photo of spherical gas storage tanks at a refinery" style="background:linear-gradient(180deg,#9cc2de,#6b8a9a 50%,#3c4c52)"></div><h4>OIL &amp; GAS</h4></div>
  <div class="abs chem-card" style="left:793px;width:352px"><div class="media" role="img" aria-label="Photo of a shopper reading a product label in a store aisle" style="background:linear-gradient(135deg,#e7d7c8,#c9a87f 50%,#9b6f52)"></div><h4>PERSONAL CARE</h4></div>
  <div class="abs btn-dark load-btn">LOAD MORE ITEMS</div>
</section>

<section class="abs services">
  <h2 class="abs services-title display">SPECIAL<br>SERVICES</h2>
  <p class="abs services-text">We always look forward to help our customers with the best services We had many services that can almost cover all the industrial needs. We take special care during the trasportation of the products and also have different types of trasportation.</p>
  <div class="abs dots" style="left:82px;top:338px"><span class="dot light on"></span><span class="dot light"></span><span class="dot light"></span><span class="dot light"></span></div>
  <div class="abs svc-card" style="left:375px"><div class="media" role="img" aria-label="Photo of warehouse racks stacked with drums and totes" style="background:linear-gradient(180deg,#d6a95a,#5a7fa4 60%,#9c8e7a)"></div><h5>WAREHOUSE STORAGE</h5><p>Lorem ipsum is the dummy text that can be replaced later with the orginal content of the website</p><a>read more &gt;&gt;</a></div>
  <div class="abs svc-card" style="left:639px"><div class="media" role="img" aria-label="Photo of a worker moving wrapped pallets in a warehouse" style="background:linear-gradient(180deg,#b8bec4,#8a9096 60%,#6b6f72)"></div><h5>SUPPLY CHAIN SOLUTIONS</h5><p>Lorem ipsum is the dummy text that can be replaced later with the orginal content of the website</p><a>read more &gt;&gt;</a></div>
  <div class="abs svc-card" style="left:899px"><div class="media" role="img" aria-label="Photo of a freight truck on a highway through green fields" style="background:linear-gradient(180deg,#7fb2e0,#a5c2d8 45%,#6e9a4a 75%,#7c7f78)"></div><h5>ROAD FREIGHT</h5><p>Lorem ipsum is the dummy text that can be replaced later with the orginal content of the website</p><a>read more &gt;&gt;</a></div>
</section>

<section class="reach">
  <h2 class="abs reach-title">Reach your destination 100% sure and safe</h2>
  <p class="abs reach-text">Lorem ipsum is the dummy text that can be replaced later with the original content of the website Lorem ipsum is the dummy text that can be replaced later with the original content of the website</p>
  <div class="abs contact-btn">Contact Now</div>
  <div class="abs agent media" role="img" aria-label="Photo of a customer service agent wearing a headset"></div>
</section>

<div class="abs map media" role="img" aria-label="Map of North America, Europe and Africa with branch location pins"></div>

<section class="regions">
  <p class="abs regions-intro">Select your region below to place an order, request samples,<br>receive a price quote, check product availability or for general questions.</p>
  <div class="abs region-tab active" style="left:104px">NORTH AMERICA</div>
  <div class="abs region-tab" style="left:452px">EUROPE</div>
  <div class="abs region-tab" style="left:800px">ASIA</div>
  <div class="abs region-box">
    <div class="abs country" style="left:18px">
      <h6>UNITED STATES</h6>
      <div class="office"><b>Sales and Customer Service</b><span>1234 street name</span><span>Dublin, OH 12345</span><span>Tel: +1 123-456-7890</span></div>
      <div class="office"><b>Sales and Customer Service</b><span>1234 street name</span><span>Conroe, TX 12345</span><span>Tel: +1 123-456-7890</span></div>
    </div>
    <div class="abs country" style="left:350px">
      <h6>CANADA</h6>
      <div class="office"><b>Sales and Customer Service</b><span>1234 street name</span><span>Dublin, OH 12345</span><span>Tel: +1 123-456-7890</span></div>
      <div class="office"><b>Sales and Customer Service</b><span>1234 street name</span><span>Dublin, OH 12345</span><span>Tel: +1 123-456-7890</span></div>
    </div>
    <div class="abs country" style="left:685px">
      <h6>MEXICO</h6>
      <div class="office"><b>Sales and Customer Service</b><span>1234 street name</span><span>Dublin, OH 12345</span><span>Tel: +1 123-456-7890</span></div>
      <div class="office"><b>Sales and Customer Service</b><span>1234 street name</span><span>Dublin, OH 12345</span><span>Tel: +1 123-456-7890</span></div>
    </div>
  </div>
</section>

<footer>
  <div class="abs footer-col" style="left:52px"><h6>SITE MAP</h6><ul><li>Home</li><li>Products</li><li>Chemicals</li><li>Solutions</li><li>blog</li><li>contact</li></ul></div>
  <div class="abs footer-col" style="left:261px"><h6>SERVICES</h6><ul><li>Environmental Services</li><li>Chemical Blending</li><li>Packaging</li><li>Supply Chain</li><li>Technical Support</li></ul></div>
  <div class="abs footer-col" style="left:528px"><h6>ABOUT US</h6><ul><li>Who we are?</li><li>What we do?</li><li>Why choose us?</li><li>History</li></ul></div>
  <div class="abs footer-col" style="left:750px"><h6>OUR BRANCHES</h6></div>
  <div class="abs branch" style="left:750px"><b>USA</b>
    <p><svg width="9" height="12" viewBox="0 0 14 18"><path d="M7 0a7 7 0 0 0-7 7c0 5 7 11 7 11s7-6 7-11a7 7 0 0 0-7-7z" fill="#143c5a"/></svg><span>1234 street name Dublin, OH 12345</span></p>
    <p><svg width="10" height="10" viewBox="0 0 10 10"><path d="M2 0c1 0 2 2 1.5 3L3 4c1 1 2 2 3 3l1-.5c1 0 3 1 3 2 0 .5-1 1.5-2 1.5C4 10 0 6 0 2 0 1 1 0 2 0z" fill="#143c5a"/></svg><span>Tel: +1 123-456-7890</span></p>
    <p><svg width="11" height="9" viewBox="0 0 11 9"><rect width="11" height="9" fill="#143c5a"/><path d="M0 0l5.5 5L11 0" stroke="#fff" fill="none"/></svg><span>info@norvalechem.com</span></p>
  </div>
  <div class="abs branch" style="left:988px"><b>USA</b>
    <p><svg width="9" height="12" viewBox="0 0 14 18"><path d="M7 0a7 7 0 0 0-7 7c0 5 7 11 7 11s7-6 7-11a7 7 0 0 0-7-7z" fill="#143c5a"/></svg><span>1234 street name Dublin, OH 12345</span></p>
    <p><svg width="10" height="10" viewBox="0 0 10 10"><path d="M2 0c1 0 2 2 1.5 3L3 4c1 1 2 2 3 3l1-.5c1 0 3 1 3 2 0 .5-1 1.5-2 1.5C4 10 0 6 0 2 0 1 1 0 2 0z" fill="#143c5a"/></svg><span>Tel: +1 123-456-7890</span></p>
    <p><svg width="11" height="9" viewBox="0 0 11 9"><rect width="11" height="9" fill="#143c5a"/><path d="M0 0l5.5 5L11 0" stroke="#fff" fill="none"/></svg><span>info@norvalechem.com</span></p>
  </div>
  <div class="abs bottombar">© 2016 Norvale chemicals. All Rights Reserved.<br>Privacy Policy | Terms of Use</div>
  <div class="abs to-top"><svg width="18" height="12" viewBox="0 0 18 12"><path d="M9 1L1 11h16z" fill="#fff"/></svg></div>
</footer>

</body>
</html>
```